50th Anniversary Gala Save the date Postcard 8.5x5.5 inches

Looking for a 5.5x8.5 in one-sided postcard design for our annual gala. Design needs to include "Save the date" prominently with all the event information included below. Design should be light, include the colors of our logo and elegant. (almost like a wedding save the date). "Bridges of Grace" should look like its own logo.

50th Anniversary Gala at The Lodge at Birchmere Glen – “Bridges of Grace – Celebrating 50 Years of Building Community”
Thursday, October 24
6-11p
The Lodge at Birchmere Glen
Calloway Parkway, New Hyde Park, NY
Honoring – TRB Previous Presidents

Target Market(s)

Exisiting donors

Industry/Entity Type

nonprofit

Font styles to use
Serif
Script

Requirements
Must have
• Save the date prominent
Should not have
• should not have a dark background

```html
<!DOCTYPE html>
<html lang="en">
<head>
<meta charset="utf-8">
<title>Community Pathways 50th Anniversary Gala – Save the Date</title>
<link href="https://fonts.googleapis.com/css2?family=Great+Vibes&family=Roboto:wght@400;500;700&display=swap" rel="stylesheet">
<style>
  :root {
    --paper: #f7f7fb;
    --navy: #1f4a8a;
    --gold: #dcae3f;
    --green: #7cb342;
    --grey: #5d6068;
    --bloom: #cfd8ea;
    --bloom-gold: #f1e3bd;
  }
  * { margin: 0; padding: 0; box-sizing: border-box; }
  html, body { width: 776px; height: 1200px; overflow: hidden; background: var(--paper); }
  .postcard {
    position: relative;
    width: 776px;
    height: 1200px;
    overflow: hidden;
    background: var(--paper);
    font-family: "Roboto", Arial, sans-serif;
  }
  .org-name {
    position: absolute;
    left: 52px; top: 122px;
    width: 250px;
    text-align: center;
    color: var(--navy);
    font-weight: 700;
    font-size: 34px;
    line-height: 1.1;
    text-transform: uppercase;
  }
  .gala-title {
    position: absolute;
    left: 360px; top: 84px;
    width: 376px;
    text-align: center;
    color: var(--navy);
    font-weight: 700;
  }
  .gala-title .years { display: block; font-size: 80px; line-height: 1; }
  .gala-title .label { display: block; font-size: 36px; line-height: 1.2; margin-top: 6px; }
  .frame-art { position: absolute; left: 0; top: 0; }
  .save-the-date {
    position: absolute;
    left: 190px; top: 372px;
    width: 380px;
    text-align: center;
    font-family: "Great Vibes", cursive;
    color: var(--gold);
    font-size: 108px;
    line-height: 0.86;
    font-weight: 400;
  }
  .save-the-date span { display: block; }
  .event-mark {
    position: absolute;
    left: 0; top: 800px;
    width: 776px;
    text-align: center;
    font-family: "Great Vibes", cursive;
    color: var(--navy);
    font-size: 80px;
    line-height: 1;
  }
  .tagline {
    position: absolute;
    left: 0; top: 922px;
    width: 776px;
    text-align: center;
    color: var(--gold);
    font-weight: 500;
    font-size: 22px;
    line-height: 26px;
  }
  .event-date {
    position: absolute;
    left: 0; top: 980px;
    width: 776px;
    text-align: center;
    color: var(--green);
    font-weight: 500;
    font-size: 24px;
    line-height: 28px;
  }
  .time-rules { position: absolute; left: 0; top: 0; }
  .event-time {
    position: absolute;
    left: 280px; top: 1038px;
    width: 216px;
    height: 46px;
    text-align: center;
    color: var(--navy);
    font-weight: 500;
    font-size: 27px;
    line-height: 46px;
  }
  .venue {
    position: absolute;
    left: 0; top: 1112px;
    width: 776px;
    text-align: center;
  }
  .venue-name { color: var(--green); font-size: 22px; font-weight: 500; text-transform: uppercase; line-height: 26px; }
  .venue-address { color: var(--grey); font-size: 16px; margin-top: 4px; line-height: 20px; }
</style>
</head>
<body>
<main class="postcard">

  <svg class="frame-art" width="776" height="1200" viewBox="0 0 776 1200">
    <g fill="none" stroke="var(--gold)" stroke-width="1.6">
      <polygon points="312,312 540,352 560,640 346,790 198,548 222,352"/>
      <polygon points="246,334 500,306 566,520 520,760 292,742 206,520"/>
    </g>
    <ellipse class="bloom-top-left" role="img" aria-label="Blue line-drawn floral spray" cx="222" cy="382" rx="85" ry="88" fill="var(--bloom)" opacity="0.7"/>
    <ellipse class="bloom-right" role="img" aria-label="Blue line-drawn floral spray" cx="560" cy="660" rx="96" ry="150" fill="var(--bloom)" opacity="0.7"/>
    <ellipse class="bloom-corner-left" role="img" aria-label="Gold floral sprig" cx="56" cy="1110" rx="44" ry="66" fill="var(--bloom-gold)"/>
    <ellipse class="bloom-corner-right" role="img" aria-label="Gold floral sprig" cx="720" cy="1110" rx="44" ry="66" fill="var(--bloom-gold)"/>
  </svg>

  <div class="org-name">Community<br>Pathways</div>

  <h1 class="gala-title">
    <span class="years">50TH</span>
    <span class="label">ANNIVERSARY GALA</span>
  </h1>

  <h2 class="save-the-date"><span>Save</span><span>the</span><span>Date</span></h2>

  <p class="event-mark">Bridges of Grace</p>
  <p class="tagline">Celebrating 50 Years of Building Community</p>
  <p class="event-date">Thursday, October 24</p>

  <svg class="time-rules" width="776" height="1200" viewBox="0 0 776 1200">
    <g fill="none" stroke="var(--navy)" stroke-width="1.4">
      <line x1="281" y1="1034" x2="497" y2="1034"/>
      <rect x="300" y="1034" width="177" height="9"/>
      <rect x="300" y="1079" width="177" height="9"/>
      <line x1="281" y1="1088" x2="497" y2="1088"/>
    </g>
  </svg>
  <p class="event-time">6-11P</p>

  <div class="venue">
    <p class="venue-name">The Lodge at Birchmere Glen</p>
    <p class="venue-address">Calloway Parkway, New Hyde Park, NY</p>
  </div>

</main>
</body>
</html>
```